Voltara Solutions Ltd - Project for new electric vehicle charging company

Please use Voltara Solutions Ltd logo & artwork instead of Brightwell.

We would like to produce a leaflet to advertise our electric vehicle charging company to build a reputation and workflow in the local area.

We would like to use the attached logo and maintain the colour palette of the of the logo to be simple, modern and effective.

I have over 15 years experience in the electrical industry and have direct access to the latest technology in electric vehicle charging.

All quotes to remain fixed costs subject to survey of the property and maintenance options can be available.

We can also offer further remedial works to any property through our sister company Brightwell Solutions Ltd.

Target Market(s)

Domestic / commercial customers

Requirements
Must have
• Voltara Solutions Ltd logo and colour palette.
Should not have
• Brightwell logo, Email or website address.

```html
<!DOCTYPE html>
<html lang="en">
<head>
<meta charset="utf-8">
<title>Voltara Solutions Ltd – EV Charging Leaflet</title>
<link rel="stylesheet" href="https://fonts.googleapis.com/css2?family=Montserrat:ital,wght@0,400;0,500;0,600;0,700;0,800;1,900&display=swap">
<style>
  :root {
    --teal: #00bcaa;
    --black: #000000;
    --white: #ffffff;
    --grey-band: #d2d3d5;
    --photo-light: #eef0f1;
    --photo-mid: #c9cdd0;
  }
  * { box-sizing: border-box; margin: 0; padding: 0; }
  html, body { width: 845px; height: 1200px; overflow: hidden; background: #b3b3b3; }
  .leaflet {
    position: relative; width: 845px; height: 1200px; overflow: hidden;
    background: var(--black); color: var(--white);
    font-family: "Montserrat", sans-serif;
  }
  .hero-shape { position: absolute; left: 0; top: 0; width: 845px; height: 340px; }

  .brand { position: absolute; left: 567px; top: 52px; width: 250px; text-align: center; }
  .brand-dot { width: 64px; height: 64px; border-radius: 50%; background: var(--teal); margin: 0 auto 14px; }
  .brand-name { font-size: 42px; font-weight: 400; color: var(--teal); line-height: 1; letter-spacing: -0.5px; }

  .headline { position: absolute; left: 32px; top: 345px; font-size: 32px; font-weight: 400; line-height: 41px; }
  .headline strong { font-weight: 700; }
  .subline { position: absolute; left: 32px; top: 488px; font-size: 20.5px; line-height: 26px; color: var(--teal); }

  .intro-band { position: absolute; left: 0; top: 567px; width: 845px; height: 315px; background: var(--teal); }
  .intro-title { position: absolute; left: 32px; top: 584px; font-size: 32px; line-height: 40px; font-weight: 400; }
  .intro-title strong { font-weight: 800; }
  .intro-lead { position: absolute; left: 32px; top: 680px; width: 448px; font-size: 13.6px; line-height: 20px; font-weight: 600; }
  .intro-rule { position: absolute; left: 32px; top: 748px; width: 447px; height: 1px; background: var(--white); }
  .intro-body { position: absolute; left: 32px; top: 756px; width: 450px; font-size: 13.6px; line-height: 20px; font-weight: 400; }

  .title-band { position: absolute; left: 0; top: 882px; width: 845px; height: 101px; background: var(--grey-band); }
  .title { position: absolute; left: 32px; top: 884px; font-size: 42px; line-height: 44px; font-weight: 900; font-style: italic; letter-spacing: -1px; color: var(--black); }
  .title .accent { color: var(--teal); }

  .charger-photo {
    position: absolute; left: 500px; top: 434px; width: 345px; height: 520px;
    background: linear-gradient(90deg, transparent 0%, var(--photo-mid) 30%, var(--photo-light) 60%, var(--photo-mid) 100%);
    opacity: 0.85;
  }

  .plug-title { position: absolute; left: 32px; top: 1008px; font-size: 21px; font-weight: 700; color: var(--teal); }
  .plug-body { position: absolute; left: 32px; top: 1042px; width: 440px; font-size: 14px; line-height: 25.5px; }

  .cta { position: absolute; right: 27px; top: 1005px; text-align: right; }
  .cta-box { display: inline-block; border: 2px solid var(--white); border-radius: 3px; padding: 3px 7px; font-size: 19px; font-weight: 800; line-height: 28px; }
  .cta-phone { font-size: 37px; font-weight: 800; color: var(--teal); line-height: 46px; margin-top: 12px; letter-spacing: -0.5px; }
  .cta-line { font-size: 19px; font-weight: 500; line-height: 31px; }
</style>
</head>
<body>
<main class="leaflet">
  <svg class="hero-shape" viewBox="0 0 845 340" aria-hidden="false">
    <path fill="var(--teal)" d="M0 0 H444 C515 55 545 170 544 280 C420 262 300 252 200 276 C120 296 60 327 0 321 Z"/>
    <defs>
      <linearGradient id="photoTone" x1="0" y1="0" x2="1" y2="1">
        <stop offset="0" stop-color="#ffffff"/>
        <stop offset="1" stop-color="#dfe2e4"/>
      </linearGradient>
    </defs>
    <path role="img" aria-label="Photo of a silver electric car beside a row of charging stations"
          fill="url(#photoTone)" d="M0 192 C14 80 110 4 238 2 C330 1 398 72 428 158 C330 160 230 176 150 200 C90 220 40 230 0 225 Z"/>
  </svg>

  <div class="brand">
    <div class="brand-dot"></div>
    <div class="brand-name">Voltara</div>
  </div>

  <h1 class="headline">After you plug them in,<br>how can you be sure they’re ready<br><strong>when you need them?</strong></h1>
  <p class="subline">Now you’ll know they’re ready<br>and charged - at the lowest possible rate.</p>

  <section class="intro-band"></section>
  <h2 class="intro-title">Introducing a smart<br><strong>charge control system...</strong></h2>
  <p class="intro-lead">Now that you've decided to get rid of your gas guzzlers and add electric-powered vehicles to your fleet, welcome to a whole new world of other challenges.</p>
  <div class="intro-rule"></div>
  <p class="intro-body">To start, your facilitys electric costs will be higher, A lot higher if you don't understand how the power company charges for electricity and how you can take advantage of it to get the best rates. And what if one of your vehicles fails to charge and is unavailable for the next days work?</p>

  <div class="title-band"></div>
  <h2 class="title">THE BEST AIC EV<br><span class="accent">CHARGER STATION</span></h2>

  <div class="charger-photo" role="img" aria-label="Photo of a white rapid EV charging station with two cables and a slim charging post"></div>

  <h3 class="plug-title">All you have to do isplug in</h3>
  <p class="plug-body">VoltPilot, fleet charging control system consists of two powerful, easy-to-use, proprietary EV control management tools that will automatically reduce your electric vehicle charging costs, improve your vehicle availability and give you important operational data for better fleet management.</p>

  <div class="cta">
    <div class="cta-box">CALL US NOW!</div>
    <div class="cta-phone">(123)-555-0147</div>
    <div class="cta-line">info@voltaracharge.com</div>
    <div class="cta-line">www.voltaracharge.com</div>
  </div>
</main>
</body>
</html>
```